Financial Advisory Firm needs a custom content template for financial topics

I need a template that I can reuse often to deliver financial advice commentary on topics ranging from investments to financial planning ideas to tax planning strategies. I am hoping to get a template that is visually exciting and captures readers attention. I will use this template to regularly create new financial and tax content that I will post to social media (e.g. Brivora), my website and targeted email campaigns to current and prospective clients. The content will never be greater than 2 pages.

```html
<!DOCTYPE html>
<html lang="en">
<head>
<meta charset="utf-8">
<title>Personal CFO – Content Templates</title>
<link rel="stylesheet" href="https://fonts.googleapis.com/css2?family=Source+Sans+3:ital,wght@0,300;0,400;0,600;0,700;1,300;1,600;1,700&display=swap">
<style>
:root{
  --page:#ffffff;
  --navy-deep:#06143f;
  --navy:#0a2466;
  --navy-bar:#0b1c52;
  --royal:#2172c0;
  --royal-dark:#1a5ea5;
  --gold:#f3d36e;
  --white:#ffffff;
  --soft:rgba(255,255,255,.72);
  --faint:rgba(255,255,255,.55);
}
*{margin:0;padding:0;box-sizing:border-box}
html,body{width:1200px;height:2298px;overflow:hidden;background:var(--page)}
body{position:relative;font-family:"Source Sans 3",sans-serif;color:var(--white)}
.panel{position:absolute;left:41px;width:1119px;height:701px;overflow:hidden}
.panel--one{top:56px;background:var(--navy-deep)}
.panel--two{top:784px;background:var(--royal)}
.panel--three{top:1546px;background:var(--royal)}
.abs{position:absolute}
.backdrop{position:absolute;inset:0}
.backdrop--money{background:radial-gradient(ellipse at 38% 48%,#1c6fc4 0%,#0d3a8f 35%,#071f5e 65%,#061540 100%)}
.photo-hands-left{left:0;top:0;width:560px;height:451px;background:linear-gradient(135deg,#0c0f16 0%,#1d2533 45%,#31435a 75%,#3e5a78 100%)}
.photo-hands-right{left:560px;top:0;width:559px;height:451px;background:linear-gradient(135deg,#5f89ad 0%,#3f6e9d 50%,#2d5f96 100%)}
.portrait{left:737px;width:382px;background:linear-gradient(180deg,#6b8fb8 0%,#3f6fae 60%,#2f62a8 100%)}
.panel--one .portrait{top:37px;height:353px}
.panel--two .portrait{top:36px;height:372px;background:linear-gradient(180deg,#6f93bb 0%,#4576b3 60%,#3568ad 100%)}
.website{left:58px;top:22px;font-size:33px;font-weight:400}
.website--bold{font-weight:700;font-style:italic;font-size:29px;top:24px}
.headline{left:58px;line-height:1.1}
.headline--gold{top:210px;color:var(--gold);font-weight:700;font-size:52px;line-height:66px}
.headline--white{top:156px;font-weight:700;font-size:52px;line-height:52px}
.headline--mixed{top:160px;font-size:50px;line-height:50px}
.headline--mixed strong{font-weight:700}
.headline--mixed span{font-weight:300}
.rule{left:62px;width:61px;height:2px;background:var(--white)}
.body{left:62px;font-size:15px;line-height:20px;width:410px}
.body--large{font-size:19px;line-height:23.5px;width:405px}
.note{left:62px;font-size:12px;line-height:17px;color:var(--faint);font-weight:300}
.note--large{font-size:15px;line-height:20px;width:370px}
.name-bar{left:684px;width:435px;height:43px;background:var(--navy-bar);font-weight:700;font-style:italic;font-size:27px;line-height:43px;padding-left:24px;white-space:nowrap}
.name-bar sup{font-size:14px}
.info-box{left:620px;top:432px;width:499px;height:154px;background:rgba(4,14,48,.86);padding:12px 36px}
.info-box .lead{font-size:14.5px;font-weight:700;line-height:18px;width:400px}
.info-box .small{margin-top:18px;font-size:11.5px;line-height:16.5px;color:var(--faint);font-weight:300;width:400px}
.bottom-band{left:0;top:451px;width:1119px;height:250px;background:var(--royal)}
.quote{left:567px;top:473px;width:490px;font-size:15px;line-height:20px;color:var(--soft);font-weight:300}
.quote-lead{left:567px;top:574px;font-size:12.5px;line-height:17px;font-weight:600}
.contact{display:flex;align-items:center;gap:8px;font-size:18px;white-space:nowrap}
.contact svg{width:19px;height:17px;flex:none}
.contact-row{display:flex;align-items:center;gap:22px;white-space:nowrap}
.contact-row .contact{font-size:17px}
.brand-square{width:13px;height:13px;border:1.5px solid var(--white);flex:none}
.avatar-ring{left:638px;top:98px;width:380px;height:380px;border-radius:50%;background:var(--royal-dark);overflow:hidden}
.avatar-ring .figure{position:absolute;left:50px;top:20px;width:280px;height:360px;border-radius:140px 140px 0 0;background:linear-gradient(180deg,#7a99c0 0%,#4a7cbd 60%,#3a6fb7 100%)}
.card-name{left:578px;width:500px;text-align:center;top:498px;font-size:34px;font-weight:700;font-style:italic;white-space:nowrap}
.card-name sup{font-size:16px}
.card-role{left:578px;width:500px;text-align:center;top:551px;font-size:22px;font-weight:300;font-style:italic;letter-spacing:5px}
.card-blurb{left:628px;width:400px;text-align:center;top:584px;font-size:12px;line-height:17px;color:var(--faint);font-weight:300}
</style>
</head>
<body>

<svg width="0" height="0" style="position:absolute">
  <defs>
    <symbol id="icon-phone" viewBox="0 0 20 18">
      <path d="M2 5c0-2 3-3 8-3s8 1 8 3v2h-4V5.5c-1-.4-2.5-.6-4-.6s-3 .2-4 .6V7H2z" fill="none" stroke="#fff" stroke-width="1.4"/>
      <rect x="4" y="8" width="12" height="8" rx="1" fill="none" stroke="#fff" stroke-width="1.4"/>
      <circle cx="10" cy="12" r="2" fill="none" stroke="#fff" stroke-width="1.2"/>
    </symbol>
    <symbol id="icon-mail" viewBox="0 0 20 16">
      <rect x="1.5" y="2" width="17" height="12" fill="none" stroke="#fff" stroke-width="1.4"/>
      <path d="M1.5 2l8.5 7 8.5-7M1.5 14l6-5.5M18.5 14l-6-5.5" fill="none" stroke="#fff" stroke-width="1.4"/>
    </symbol>
  </defs>
</svg>

<section class="panel panel--one">
  <div class="backdrop backdrop--money" role="img" aria-label="Deep blue photograph of banknotes"></div>
  <div class="abs website website--bold">www.northplancfo.com</div>
  <h1 class="abs headline headline--gold">Money is mean, not en end<br>what are your life goal ?</h1>
  <div class="abs rule" style="top:385px"></div>
  <p class="abs body" style="top:432px">Lorem ipsum dolor sit amet, consectetuer adipiscing elit, sed diam nonummy nibh euismod tincidunt ut laoreet dolore magna aliquam erat volutpat. Ut wisi enim ad minim veniam, quis nostrud exerci tation ullamcorper suscipit lobortis nisl ut aliquip ex ea commodo consequat.</p>
  <p class="abs note" style="top:568px">Lorem ipsum dolor sit amet,<br>consectetuer adipiscing elit, sed diam</p>
  <div class="abs portrait" role="img" aria-label="Portrait photo of the advisor in a blue blazer"></div>
  <div class="abs name-bar" style="top:390px">Daniel Halvorsen, CFP<sup>®</sup>, CPA</div>
  <div class="abs info-box">
    <p class="lead">Lorem ipsum dolor sit amet, consectetuer adipiscing elit, sed diam nonummy.</p>
    <p class="small">Lorem ipsum dolor sit amet, consectetuer adipiscing elit, sed diam nonummy nibh euismod tincidunt ut laoreet dolore magna aliquam erat volutpat. Ut wisi enim ad minim veniam, consequat. Duis autem vel eum iriure</p>
  </div>
  <div class="abs contact" style="left:638px;top:609px"><svg><use href="#icon-phone"/></svg>555-014-2870</div>
  <div class="abs contact" style="left:638px;top:634px"><svg><use href="#icon-mail"/></svg>daniel@northplancfo.com</div>
  <div class="abs contact" style="left:890px;top:609px"><span class="brand-square"></span>Brivora</div>
</section>

<section class="panel panel--two">
  <div class="abs photo-hands-left" role="img" aria-label="Dark photo of a hand holding out a payment card"></div>
  <div class="abs photo-hands-right" role="img" aria-label="Blue-toned photo of a hand receiving the card"></div>
  <div class="abs website">www.northplancfo.com</div>
  <h1 class="abs headline headline--white">Do have a plan ?<br>Are you<br>accecuting on it ?</h1>
  <div class="abs rule" style="top:384px"></div>
  <div class="abs portrait" role="img" aria-label="Portrait photo of the advisor in a blue blazer"></div>
  <div class="abs name-bar" style="top:408px">Daniel Halvorsen, CFP<sup>®</sup>, CPA</div>
  <div class="abs bottom-band"></div>
  <p class="abs body body--large" style="top:473px">Lorem ipsum dolor sit amet, consectetuer adipiscing elit, sed diam nonummy nibh euismod tincidunt ut laoreet dolore magna aliquam erat volutpat. Ut wisi enim ad minim veniam, quis</p>
  <p class="abs note" style="top:604px">Lorem ipsum dolor sit amet,<br>consectetuer adipiscing elit, sed diam</p>
  <p class="abs quote">“Lorem ipsum dolor sit amet, consectetuer adipiscing elit, sed diam nonummy nibh euismod tincidunt ut laoreet dolore magna aliquam erat volutpat”</p>
  <p class="abs quote-lead">Lorem ipsum dolor sit amet, consectetuer adipiscing elit,<br>sed diam nonummy nibh euismod tincidunt.</p>
  <div class="abs contact-row" style="left:567px;top:659px">
    <div class="contact"><svg><use href="#icon-phone"/></svg>555-014-2870</div>
    <div class="contact"><svg><use href="#icon-mail"/></svg>daniel@northplancfo.com</div>
    <div class="contact"><span class="brand-square"></span>Brivora</div>
  </div>
</section>

<section class="panel panel--three">
  <div class="abs website">www.northplancfo.com</div>
  <h1 class="abs headline headline--mixed"><strong>Stop Procastinating.</strong><br><span>Take control of your<br>finacial future.</span></h1>
  <div class="abs rule" style="top:358px"></div>
  <p class="abs body body--large" style="top:398px">Lorem ipsum dolor sit amet, consectetuer adipiscing elit, sed diam nonummy nibh euismod tincidunt ut laoreet dolore magna aliquam erat volutpat. Ut wisi enim ad minim veniam, quis</p>
  <p class="abs note note--large" style="top:520px">Lorem ipsum dolor sit amet, consectetuer adipiscing elit, sed diam nonummy nibh euismod tincidunt ut laoreet dolore magna aliquam erat volutpat. Ut wisi</p>
  <div class="abs avatar-ring">
    <div class="figure" role="img" aria-label="Portrait photo of the advisor in a blue blazer"></div>
  </div>
  <div class="abs card-name">Daniel Halvorsen, CFP<sup>®</sup>, CPA</div>
  <div class="abs card-role">Personal CFO</div>
  <p class="abs card-blurb">Lorem ipsum dolor sit amet, consectetuer adipiscing elit, sed diam nonummy nibh euismod tincidunt.</p>
  <div class="abs contact-row" style="left:56px;top:659px">
    <div class="contact"><svg><use href="#icon-phone"/></svg>555-014-2870</div>
    <div class="contact"><svg><use href="#icon-mail"/></svg>daniel@northplancfo.com</div>
    <div class="contact"><span class="brand-square"></span>Brivora</div>
  </div>
</section>

</body>
</html>
```